New management consulting website

I need a 4-5 page website that I can manage in WordPress on Hostlane.example for a new management consulting company. The website is www.torvik-example.com and the company name is Torvik Group LLC. The attached spec has an example of a draft site, layout and actual copy and includes company and contact information. I have more high-res images I can send.

Must include instruction/assistance loading the site to my WordPress dashboard.

Target Market(s)

Any business, especially SAAS

Industry/Entity Type

Consultant

Coding

Coded - Design and coding required

Number of Pages Required

4 page

Font styles to use
Sans Serif

Colors
0456a4

Requirements
Must have
• Modern and stylish

```html
<!DOCTYPE html>
<html lang="en">
<head>
<meta charset="utf-8">
<title>Torvik Consulting</title>
<link href="https://fonts.googleapis.com/css2?family=Mulish:wght@400;500;600;700;800&display=swap" rel="stylesheet">
<style>
:root{
  --navy:#1f3f6d;
  --navy-deep:#16304f;
  --ink:#1c1c1c;
  --muted:#555b66;
  --grey-band:#d9d9d9;
  --white:#ffffff;
  --line:#c9ccd2;
}
*{box-sizing:border-box;margin:0;padding:0}
html,body{width:1200px;height:3916px;overflow:hidden}
body{position:relative;background:var(--white);font-family:"Mulish",Arial,sans-serif;color:var(--ink)}
.abs{position:absolute}
a{color:inherit;text-decoration:none}

/* header */
.brand{left:144px;top:14px;width:232px;text-align:center;color:var(--navy)}
.brand-name{font-size:48px;font-weight:700;letter-spacing:1px;line-height:48px}
.brand-sub{font-size:15px;letter-spacing:2px;color:#8a93a3;border-top:1px solid #8a93a3;margin-top:2px;padding-top:1px}
.contact-top{top:10px;font-size:15px;color:var(--navy);display:flex;align-items:center;gap:10px}
.contact-top .ring{width:30px;height:30px;border:1.5px solid #8a93a3;border-radius:50%;display:flex;align-items:center;justify-content:center}
.main-nav{top:58px;right:142px;display:flex;gap:34px;font-size:15px;color:var(--ink)}
.main-nav .active{color:var(--navy);font-weight:700}

/* hero */
.hero-text{left:676px;top:260px;color:#fff;font-size:25px;line-height:32px;text-shadow:0 1px 3px rgba(0,0,0,.35)}
.btn-outline{left:676px;top:365px;width:148px;height:42px;background:var(--navy-deep);border:1px solid #fff;color:#fff;font-size:13px;font-weight:700;display:flex;align-items:center;justify-content:center}
.scroll-ring{left:560px;top:546px;width:82px;height:82px;border-radius:50%;background:#fff;border:2px solid #cfd5de;box-shadow:0 0 0 6px rgba(255,255,255,.6);display:flex;align-items:center;justify-content:center}

/* shared */
.rule{width:48px;height:3px;background:#8a93a3}
.btn{background:var(--navy);color:#fff;font-size:15px;display:flex;align-items:center;justify-content:center;border-radius:2px}
.photo{display:block}

/* about */
.about-title{left:141px;top:790px;font-size:33px;font-weight:700;color:var(--navy)}
.about-copy{left:141px;top:862px;width:470px;font-size:12.5px;line-height:23px;color:var(--ink)}
.about-copy p{margin-bottom:8px}
.about-copy .lead{font-size:14px;line-height:25px}

/* services */
.services-title{left:0;width:1200px;top:1432px;text-align:center;color:#fff;font-size:32px;font-weight:700}
.services-intro{left:200px;width:800px;top:1498px;text-align:center;color:#fff;font-size:12.5px;line-height:23px}
.card{top:1568px;width:222px;height:297px;background:#fff;border-radius:6px;text-align:center;padding-top:22px}
.card .ico{width:92px;height:92px;margin:0 auto;border-radius:50%;background:#eef1f6;border:2px solid #c9d1dd;display:flex;align-items:center;justify-content:center}
.card h3{font-size:15px;font-weight:800;margin-top:26px;color:var(--ink)}
.card p{font-size:14px;line-height:23px;color:var(--ink);margin-top:12px;padding:0 16px}
.card a{display:inline-block;margin-top:16px;font-size:15px;text-decoration:underline}

/* team */
.team-copy{left:587px;top:2212px;width:470px}
.team-copy h2{font-size:32px;color:var(--navy);font-weight:700}
.team-copy h3{font-size:25px;color:var(--navy);font-weight:700;margin-top:22px}
.team-copy .role{font-size:12px;color:var(--navy);font-weight:700}
.team-copy p{font-size:12.5px;line-height:23px;margin-top:12px}

/* form */
.form-card{left:281px;top:2686px;width:636px;height:546px;background:#fff;border-top:3px solid var(--navy);box-shadow:0 0 24px rgba(0,0,0,.12)}
.form-card h2{text-align:center;font-size:32px;color:var(--navy);font-weight:700;margin-top:34px}
.form-card .intro{text-align:center;font-size:12.5px;line-height:23px;width:530px;margin:16px auto 0}
.field{position:absolute;width:252px;border-bottom:1px solid var(--line);padding-bottom:10px}
.field label{display:block;font-size:12px;color:var(--ink)}
.field span{display:block;font-size:13px;color:#777;margin-top:9px}
.submit{left:53px;top:453px;width:134px;height:42px;font-size:13px;font-weight:700;border-radius:0}
.form-brand{right:50px;top:432px;width:232px;text-align:center;color:#8a93a3}

/* contact details */
.details-title{left:0;width:1200px;top:3475px;text-align:center;color:#fff;font-size:32px}
.details-sub{left:0;width:1200px;top:3548px;text-align:center;color:#fff;font-size:14px}
.tile{top:3590px;width:212px;height:176px;border:1px solid rgba(255,255,255,.3);text-align:center;color:#fff;padding-top:30px}
.tile h4{font-size:16px;font-weight:600;margin-top:12px}
.tile p{font-size:12.5px;line-height:20px;margin-top:6px}

/* footer */
.site-footer{left:0;top:3856px;width:1200px;height:60px;background:var(--navy);color:#fff;font-size:13px}
.site-footer .copy{position:absolute;left:141px;top:20px}
.site-footer nav{position:absolute;right:142px;top:20px;display:flex;gap:18px}
</style>
</head>
<body>

<!-- header -->
<div class="abs brand"><div class="brand-name">TORVIK</div><div class="brand-sub">CONSULTING</div></div>
<div class="abs contact-top" style="left:735px">
  <span class="ring"><svg width="16" height="16" viewBox="0 0 24 24" fill="none" stroke="#1f3f6d" stroke-width="2"><path d="M5 3h4l2 5-3 2a11 11 0 0 0 6 6l2-3 5 2v4a2 2 0 0 1-2 2A17 17 0 0 1 3 5a2 2 0 0 1 2-2z"/></svg></span>555.014.0192
</div>
<div class="abs contact-top" style="left:905px;font-size:13px">
  <span class="ring"><svg width="16" height="16" viewBox="0 0 24 24" fill="none" stroke="#1f3f6d" stroke-width="2"><rect x="3" y="6" width="18" height="13"/><path d="M3 7l9 7 9-7"/></svg></span>info@torvik-example.com
</div>
<nav class="abs main-nav"><a class="active">Home</a><a>About Us</a><a>Services</a><a>Contact Us</a></nav>

<!-- hero -->
<svg class="abs" style="left:0;top:88px" width="1200" height="610" viewBox="0 88 1200 610" role="img" aria-label="Silhouette of a climber helping another up a mountain ridge at dawn">
  <defs>
    <linearGradient id="heroSky" x1="0" y1="0" x2="0" y2="1">
      <stop offset="0" stop-color="#5f86b4"/><stop offset=".45" stop-color="#a9c0d8"/><stop offset="1" stop-color="#1c3a62"/>
    </linearGradient>
  </defs>
  <polygon points="0,88 1200,88 1200,540 0,622" fill="url(#heroSky)"/>
  <polygon points="220,612 1200,538 1200,560 220,630" fill="var(--grey-band)"/>
  <polygon points="800,596 1200,545 1200,692" fill="var(--navy)"/>
</svg>
<div class="abs hero-text">Our Approach<br>Is To Help You Rise Above Your<br>Day-to-day Business Challenges</div>
<a class="abs btn-outline">Contact Us Today</a>
<div class="abs scroll-ring"><svg width="26" height="22" viewBox="0 0 26 22" fill="none" stroke="#1f3f6d" stroke-width="2"><path d="M3 3l10 8 10-8M3 11l10 8 10-8"/></svg></div>

<!-- about -->
<h2 class="abs about-title">ABOUT TORVIK CONSULTING</h2>
<div class="abs rule" style="left:141px;top:840px"></div>
<div class="abs about-copy">
  <p class="lead">The word ‘Torvik’ originates from old Northumbrian English language and means ‘above, beyond’.</p>
  <p>At Torvik Consulting our approach is to help you rise above your day-to-day business challenges, and build unique, innovative solutions to move beyond them.</p>
  <p>Lorem ipsum dolor sit amet, consectetuer adipiscing elit, sed diam ummy nibh euismod tincidunt ut laoreet dlore magna aliquam erat volutpat. Ut wisifd fenim ad minim veniam, quiLorem ipsum dolor sit amet.</p>
</div>
<a class="abs btn" style="left:140px;top:1066px;width:116px;height:42px">Read More</a>
<div class="abs photo" role="img" aria-label="Two business colleagues discussing charts at an office desk" style="left:659px;top:750px;width:401px;height:382px;background:linear-gradient(135deg,#dfe6ee,#9fb0c3 60%,#2c3a4f)"></div>
<div class="abs" style="left:683px;top:774px;width:401px;height:383px;border:2px solid var(--navy)"></div>

<!-- services -->
<svg class="abs" style="left:0;top:1216px" width="1200" height="930" viewBox="0 1216 1200 930" role="img" aria-label="Hikers silhouetted on a mountain ridge at sunset">
  <defs>
    <linearGradient id="svcSky" x1="0" y1="0" x2="0" y2="1">
      <stop offset="0" stop-color="#1b365c"/><stop offset=".55" stop-color="#5a6b80"/><stop offset=".8" stop-color="#8a7356"/><stop offset="1" stop-color="#1d1d20"/>
    </linearGradient>
  </defs>
  <polygon points="0,1216 0,1340 400,1312" fill="var(--navy)"/>
  <polygon points="0,1340 980,1275 980,1292 0,1358" fill="var(--grey-band)"/>
  <polygon points="0,1358 1200,1272 1200,2002 0,2070" fill="url(#svcSky)"/>
  <polygon points="220,2077 1200,1997 1200,2020 220,2097" fill="var(--grey-band)"/>
  <polygon points="800,2046 1200,2004 1200,2145" fill="var(--navy)"/>
</svg>
<h2 class="abs services-title">Our Services</h2>
<div class="abs rule" style="left:575px;top:1484px;width:50px;background:#fff"></div>
<p class="abs services-intro">Lorem ipsum dolor sit amet, consectetuer adipiscing elit, sed diam nonummy nibh euismod tincidunt ut laoreet dlore magna aliquam erat volutpat. Ut wisifd fenim ad minim veniam, quis.</p>

<div class="abs card" style="left:140px">
  <div class="ico"><svg width="44" height="44" viewBox="0 0 24 24" fill="none" stroke="#1f3f6d" stroke-width="1.5"><circle cx="12" cy="12" r="4"/><path d="M12 2v3M12 19v3M2 12h3M19 12h3M5 5l2 2M17 17l2 2M5 19l2-2M17 7l2-2"/></svg></div>
  <h3>Strategy &amp; Operations</h3><p>Lorem ipsum dolor sit amet, consectetuer adipiscing elit, sed diam nonummy....</p><a>Read More</a>
</div>
<div class="abs card" style="left:373px">
  <div class="ico"><svg width="44" height="44" viewBox="0 0 24 24" fill="none" stroke="#1f3f6d" stroke-width="1.5"><circle cx="10" cy="10" r="7"/><path d="M15 15l6 6M6 12l3-3 2 2 3-4"/></svg></div>
  <h3>Data Analysis &amp; Insights</h3><p>Lorem ipsum dolor sit amet, consectetuer adipiscing elit, sed diam nonummy....</p><a>Read More</a>
</div>
<div class="abs card" style="left:606px">
  <div class="ico"><svg width="44" height="44" viewBox="0 0 24 24" fill="#1f3f6d"><circle cx="9" cy="4" r="2"/><path d="M7 7h4l2 4-2 1-1-2-1 3 2 4H9l-2-3-2 3H3l3-5 1-4-2 2-1-1z"/><path d="M13 21v-3h3v-3h3v-3h3v9z"/></svg></div>
  <h3>Leadership Development</h3><p>Lorem ipsum dolor sit amet, consectetuer adipiscing elit, sed diam nonummy....</p><a>Read More</a>
</div>
<div class="abs card" style="left:838px">
  <div class="ico"><svg width="44" height="44" viewBox="0 0 24 24" fill="#1f3f6d"><circle cx="12" cy="5" r="2"/><circle cx="5" cy="11" r="2"/><circle cx="19" cy="11" r="2"/><path d="M10 8h4v6h-4zM3 14h4v5H3zM17 14h4v5h-4z"/></svg></div>
  <h3>Executive Leadership</h3><p>Lorem ipsum dolor sit amet, consectetuer adipiscing elit, sed diam nonummy....</p><a>Read More</a>
</div>

<!-- team -->
<div class="abs photo" role="img" aria-label="Portrait of the founder standing in a bright office" style="left:141px;top:2173px;width:400px;height:382px;background:linear-gradient(90deg,#eef3f8,#d7e2ec 50%,#f4f7fa)"></div>
<div class="abs" style="left:116px;top:2198px;width:401px;height:383px;border:2px solid var(--navy)"></div>
<div class="abs team-copy">
  <h2>Our Team</h2>
  <div class="rule" style="margin-top:10px"></div>
  <h3>Daniel Reeve</h3>
  <div class="role">Founder &amp; Senior Consultant</div>
  <p>Lorem ipsum dolor sit amet, consectetuer adipiscing elit, sed diam ummy nibh euismod tincidunt ut laoreet dlore magna aliquam erat volutpat. Ut wisifd fenim ad minim veniam, quis.</p>
  <p>Lorem ipsum dolor sit amet, consectetuer adipiscing elit, sed diam ummy nibh euismod tincidunt ut laoreet dlore magna aliquam erat volutpat. Ut wisifd fenim ad minim veniam, quiLorem ipsum dolor sit amet.</p>
</div>
<a class="abs btn" style="left:587px;top:2492px;width:117px;height:42px">Read More</a>

<!-- contact form -->
<section class="abs form-card">
  <h2>CONTACT US NOW</h2>
  <div class="rule" style="margin:10px auto 0"></div>
  <p class="intro">Lorem ipsum dolor sit amet, consectetuer adipiscing elit, sed diam ummy nibh euismod tincidunt ut laoreet dlore magna aliquam erat volutpat.</p>
  <div class="field" style="left:50px;top:170px"><label>First Name *</label><span>Alex</span></div>
  <div class="field" style="left:334px;top:170px"><label>Last Name *</label><span>Carter</span></div>
  <div class="field" style="left:50px;top:245px"><label>Phone *</label><span>123 456 7890</span></div>
  <div class="field" style="left:334px;top:245px"><label>Email *</label><span>alex@example.com</span></div>
  <div class="field" style="left:50px;top:320px;width:536px;height:82px"><label>Message *</label><span>Type Your Message</span></div>
  <a class="abs btn submit">SUBMIT NOW</a>
  <div class="abs form-brand"><div class="brand-name" style="font-size:46px;line-height:46px">TORVIK</div><div class="brand-sub" style="color:#8a93a3">CONSULTING</div></div>
</section>

<!-- contact details -->
<svg class="abs" style="left:0;top:3278px" width="1200" height="578" viewBox="0 3278 1200 578" role="img" aria-label="Business team meeting around a table, darkened">
  <polygon points="0,3278 0,3400 400,3372" fill="var(--navy)"/>
  <polygon points="0,3424 980,3345 980,3362 0,3442" fill="var(--grey-band)"/>
  <polygon points="0,3442 1200,3348 1200,3856 0,3856" fill="#262a30"/>
</svg>
<h2 class="abs details-title">Contact Details</h2>
<div class="abs rule" style="left:575px;top:3524px;width:50px;background:#fff"></div>
<p class="abs details-sub">Speak To Us Or Send Us An Enquiry For Free Consultation.</p>
<div class="abs tile" style="left:140px">
  <svg width="36" height="44" viewBox="0 0 24 30" fill="none" stroke="#fff" stroke-width="1.6"><path d="M12 29s10-11 10-18a10 10 0 0 0-20 0c0 7 10 18 10 18z"/><circle cx="12" cy="11" r="4"/></svg>
  <h4>Address</h4><p>480 Example Ave #200<br>Springfield, ST 00000</p>
</div>
<div class="abs tile" style="left:375px">
  <svg width="40" height="44" viewBox="0 0 24 24" fill="none" stroke="#fff" stroke-width="1.4"><path d="M3 10l9-7 9 7v11H3z"/><path d="M3 10l9 6 9-6"/></svg>
  <h4>Email</h4><p>info@torvik-example.com</p>
</div>
<div class="abs tile" style="left:610px">
  <svg width="40" height="44" viewBox="0 0 24 24" fill="none" stroke="#fff" stroke-width="1.4"><path d="M5 3h4l2 5-3 2a11 11 0 0 0 6 6l2-3 5 2v4a2 2 0 0 1-2 2A17 17 0 0 1 3 5a2 2 0 0 1 2-2z"/></svg>
  <h4>Phone</h4><p style="font-size:15px">555-014-0192</p>
</div>
<div class="abs tile" style="left:846px">
  <svg width="40" height="44" viewBox="0 0 24 24"><circle cx="12" cy="12" r="9" fill="#fff"/></svg>
  <h4>SOCIAL</h4><p>social/torvikconsulting</p>
</div>

<!-- footer -->
<footer class="abs site-footer">
  <div class="copy">Copyright © 2021 Torvik Consulting.&nbsp; All Right Reserved.</div>
  <nav><a>Home</a><span>I</span><a>About Us</a><span>I</span><a>Services</a><span>I</span><a>Contact Us</a></nav>
</footer>

</body>
</html>
```